Dental Health Door hanger for contest to attract new patients

We are a group dental practice located in Burlington, Ontario, Canada. We are looking to bring in new patients and are targeting a new subdivision as well as established neighbourhoods around it.

The door hanger we require is for a contest are offering that will run for approx. 6 months to win a $1000.00 travel gift card. The individual must come in person to drop off the ballot and during that time they will get a tour of the practice and meet key people. There is no requirement for them to make an appointment but that is the ultimate goal.

I have included:
- a picture we typically use, however it is not required (female smiling)
- Our logo with "your city your dentists" below it. We want that tagline removed
- our other logo
- the excel version of the map created to our location
- the current one attempted on our own and is missing something - like the concept but not the total look/ feel

The final design should make the person want to come in and book an appointment with us and at the very least call to schedule something with a dentist.

Target Market(s)

New subdivision and surrounding area for new patients

Industry/Entity Type

Dental Clinic

Colors

Designer to choose colors to be used in the design.

Requirements
Must have
• Our address is 1846 Pemberly Road, Burlington, Ontario L7M 2K8. Our phone number is 905-482-7150. We are located on the 3rd floor of the Corvane Family Health Centre.
Nice to have
• We only need to have a logo, our address, a ballot of some sort on the door hanger and the details about the contest, the rest is up to you. We are moving towards the slogan "what makes you smile" at some point so this can be incorporated if it works with the overall design.
Should not have
• Fluorescent colours

```html
<!DOCTYPE html>
<html lang="en">
<head>
<meta charset="utf-8">
<title>Maplecrest Dental Group – Door Hanger</title>
<link rel="stylesheet" href="https://fonts.googleapis.com/css2?family=Open+Sans:wght@400;700;800&family=Signika:wght@600;700&display=swap">
<style>
  :root{
    --stage:#c5c1c0;
    --brand-blue:#176bd6;
    --map-blue:#1460c4;
    --slate:#58585a;
    --slate-dark:#4c4c4e;
    --prize-yellow:#f5e20f;
    --ink:#1d1d1f;
    --paper:#ffffff;
    --ballot:#f5f5f5;
    --wood-light:#dccbb4;
    --wood-mid:#c9b394;
  }
  *{margin:0;padding:0;box-sizing:border-box}
  html,body{width:1200px;height:1200px;overflow:hidden;background:var(--stage)}
  .stage{position:relative;width:1200px;height:1200px}
  .hanger{position:absolute;top:175px;width:378px;height:849px;overflow:hidden}
  .hanger--front{left:150px;font-family:"Open Sans",sans-serif}
  .hanger--back{left:642px;font-family:"Signika","Open Sans",sans-serif}
  .hanger svg.shapes{position:absolute;inset:0;width:378px;height:849px}
  .abs{position:absolute;left:0;width:100%;text-align:center}

  /* brand name */
  .brand{position:absolute;font-variant:small-caps;font-weight:400;color:var(--ink);white-space:nowrap;letter-spacing:.5px}
  .hanger--front .brand{top:210px;left:0;width:100%;text-align:center;font-size:30px}
  .hanger--back .brand{top:18px;left:0;width:100%;text-align:center;font-family:"Open Sans",sans-serif;font-size:17px;color:#3a3a3a}

  /* front offer */
  .offer-lead,.offer-tail{font-weight:800;color:var(--paper);font-size:32px;letter-spacing:.3px}
  .offer-lead{top:553px}
  .offer-amount{top:583px;font-weight:800;color:var(--prize-yellow);font-size:62px;letter-spacing:-1px;line-height:1.1}
  .offer-tail{top:652px}
  .phone-line{top:741px;display:flex;justify-content:center;align-items:center;gap:10px;font-weight:800;color:var(--prize-yellow);font-size:30px}
  .phone-line svg{width:26px;height:26px}
  .address-line{top:788px;display:flex;justify-content:center;align-items:center;gap:5px;font-weight:700;color:#1f4fa8;font-size:11.5px}
  .address-line svg{width:10px;height:13px}
  .web-line{top:817px;display:flex;justify-content:center;align-items:center;gap:9px;color:var(--paper);font-size:18px}
  .web-line svg{width:14px;height:14px}

  /* back */
  .invite{top:192px;color:var(--paper);font-weight:700;font-size:17px;line-height:21px}
  .details{top:462px;color:var(--ink);font-weight:600;font-size:13.4px;line-height:19.7px}
  .ballot-field{position:absolute;left:34px;width:308px;height:41px;border-bottom:1px solid #333;font-weight:700;font-size:13px;color:var(--ink)}
  .ballot-field span{position:absolute;top:6px}
  .ballot-field .right{left:179px}
</style>
</head>
<body>
<main class="stage">

  <!-- Front -->
  <section class="hanger hanger--front">
    <svg class="shapes" viewBox="0 0 378 849">
      <defs>
        <linearGradient id="photoTone" x1="0" y1="0" x2="1" y2="1">
          <stop offset="0" stop-color="#4a3a34"/>
          <stop offset=".5" stop-color="#c9a592"/>
          <stop offset="1" stop-color="#e8e2de"/>
        </linearGradient>
      </defs>
      <rect width="378" height="849" fill="var(--brand-blue)"/>
      <path d="M0 168 Q189 118 378 168 L378 177 Q189 129 0 177Z" fill="var(--slate)"/>
      <path d="M0 177 Q189 129 378 177 L378 301 Q189 253 0 301Z" fill="var(--paper)"/>
      <path d="M0 301 Q189 253 378 301 L378 294 Q189 244 0 294Z" fill="var(--slate)"/>
      <path d="M0 301 Q189 253 378 301 L378 489 Q189 553 0 489Z" fill="url(#photoTone)" role="img" aria-label="Photo of a smiling young woman in a winter hat"/>
      <path d="M0 489 Q189 553 378 489 L378 497 Q189 563 0 497Z" fill="var(--slate)"/>
      <rect y="537" width="378" height="169" fill="var(--slate)"/>
      <polygon points="66,737 314,737 342,783 34,783" fill="var(--slate)"/>
      <rect y="783" width="378" height="29" fill="var(--paper)"/>
      <polygon points="10,812 368,812 378,830 378,849 0,849 0,830" fill="var(--slate)"/>
      <circle cx="189" cy="106" r="56" fill="#d9d9d9"/>
      <circle cx="189" cy="106" r="50" fill="var(--paper)"/>
    </svg>

    <div class="brand">Maplecrest Dental Group</div>

    <div class="abs offer-lead">ENTER TO WIN A</div>
    <div class="abs offer-amount">$1000</div>
    <div class="abs offer-tail">TRAVEL GIFT CARD</div>

    <div class="abs phone-line">
      <svg viewBox="0 0 24 24"><path fill="#fff" d="M6.6 10.8a15.1 15.1 0 0 0 6.6 6.6l2.2-2.2c.3-.3.7-.4 1-.2 1.1.4 2.3.6 3.6.6.6 0 1 .4 1 1V20c0 .6-.4 1-1 1A17 17 0 0 1 3 4c0-.6.4-1 1-1h3.5c.6 0 1 .4 1 1 0 1.3.2 2.5.6 3.6.1.3 0 .7-.2 1z"/></svg>
      905-482-7150
    </div>
    <div class="abs address-line">
      <svg viewBox="0 0 10 13"><path fill="#1f4fa8" d="M5 0a5 5 0 0 0-5 5c0 3.5 5 8 5 8s5-4.5 5-8a5 5 0 0 0-5-5zm0 7a2 2 0 1 1 0-4 2 2 0 0 1 0 4z"/></svg>
      1846 Pemberly Road, Burlington, Ontario L7M 2K8
    </div>
    <div class="abs web-line">
      <svg viewBox="0 0 14 14" fill="none" stroke="#fff" stroke-width="1.1"><circle cx="7" cy="7" r="6"/><ellipse cx="7" cy="7" rx="2.6" ry="6"/><path d="M1 7h12M2 4h10M2 10h10"/></svg>
      www.maplecrestdental.ca
    </div>
  </section>

  <!-- Back -->
  <section class="hanger hanger--back">
    <svg class="shapes" viewBox="0 0 378 849">
      <defs>
        <linearGradient id="woodTone" x1="0" y1="0" x2="1" y2="0">
          <stop offset="0" stop-color="var(--wood-mid)"/>
          <stop offset=".5" stop-color="var(--wood-light)"/>
          <stop offset="1" stop-color="var(--wood-mid)"/>
        </linearGradient>
      </defs>
      <rect width="378" height="629" fill="url(#woodTone)" role="img" aria-label="Light wood grain texture"/>
      <path d="M0 57 Q189 153 378 57 L378 67 Q189 165 0 67Z" fill="var(--slate)"/>
      <path d="M0 216 Q189 116 378 216 L378 225 Q189 129 0 225Z" fill="var(--slate)"/>
      <path d="M0 225 Q189 129 378 225 L378 389 Q189 493 0 389Z" fill="var(--brand-blue)"/>
      <path d="M0 389 Q189 493 378 389 L378 402 Q189 508 0 402Z" fill="var(--slate)"/>
      <rect x="90" y="262" width="196" height="166" fill="var(--map-blue)" role="img" aria-label="Street map showing the clinic location near the main intersection"/>
      <rect y="629" width="378" height="9" fill="var(--brand-blue)"/>
      <rect y="638" width="378" height="13" fill="var(--slate)"/>
      <rect y="651" width="378" height="198" fill="var(--ballot)"/>
      <circle cx="190" cy="106" r="56" fill="#d9d9d9"/>
      <circle cx="190" cy="106" r="50" fill="var(--paper)"/>
    </svg>

    <div class="brand">Maplecrest Dental Group</div>

    <div class="abs invite">Stop By<br>Meet The Team<br>Enter To Win!</div>

    <div class="abs details">
      Come in person to submit your ballot at our<br>
      Pemberly Road location, conveniently<br>
      located on the 3rd floor of the<br>
      Corvane Family Health Centre<br>
      1846 Pemberly Road<br>
      905-482-7150<br>
      www.maplecrestdental.ca<br>
      Contest closes July 15, 2019
    </div>

    <div class="ballot-field" style="top:654px"><span>Name</span></div>
    <div class="ballot-field" style="top:695px"><span>Address</span></div>
    <div class="ballot-field" style="top:736px"><span>City</span><span class="right">Postal Code</span></div>
    <div class="ballot-field" style="top:777px"><span>Phone</span></div>
    <div class="ballot-field" style="top:818px;border-bottom:none"><span>Email Address</span></div>
  </section>

</main>
</body>
</html>
```